Our Pantry Remedy

I am a pharmacist turn chef and my current website www.ourpantryremedy.example is in desperate need of a make over. I want to be able to add how to videos, photographs and have tabs. The tabs needed will be Home, About, Recipes, Health & Wellness, Services, Confidentiality, Affordability, Blog, Articles and Friday Cocktails. Eventually I will want a news letter, but do not want that now, only the ability to add it later. I will also want to add a market place tab later to sell merchandise and ebooks. The ability to navigate should be easy and not confusing and the ability to post should be easy. I will need social media Friendloop, Pinvora, zemlo plus, zemlo, Snapcove and chirpel. In addition I will need some direction on how to operate the site. Examples of website I like (but do not want to copy) are www.buildfinewell.example www.drpetermarvell.example. It is best for me to work with someone who can explain things simply.

Another website I think is nice is www.tbgalley.example  Thanks!

Target Market(s)

The business will be diving right into the delicious side of Key West’s good health as a personal chef, a culinary wellness coach, a wellness cooking teacher, a healthful caterer and a wellness host and entertainer.
The site needs to promote health with the art of food because I am convinced that health is best enhanced, maintained and recovered through nutritious eating and cuisine, and not through pills.
I will be infusing fresh recipes with a Key West flair in hopes to share my passion and insights into nutrition and health with residents and visitors alike. I want everyone to feel welcome to come in and join the fun.

Industry/Entity Type

Chef

Colors

Designer to choose colors to be used in the design.

Requirements
Must have
• Easy navigation, easy operation and posting and social media tools. Spam filters to keep the creeps away and important plugins that make it all work.
Nice to have
• Everything is nice to have

```html
<!DOCTYPE html>
<html lang="en">
<head>
<meta charset="utf-8">
<title>Our Pantry Remedy</title>
<link href="https://fonts.googleapis.com/css2?family=Asap:wght@400;500;700&family=Arimo:wght@400;700&display=swap" rel="stylesheet">
<style>
:root{
  --orange:#f0602a;
  --green:#0b7a3e;
  --dark:#3b3b3b;
  --text:#6b6b6b;
  --light:#e4e4e4;
  --white:#ffffff;
}
*{box-sizing:border-box;margin:0;padding:0}
html,body{width:744px;height:1200px;overflow:hidden;background:var(--white)}
body{position:relative;font-family:"Asap",sans-serif;color:var(--text)}
.abs{position:absolute}

.topbar{left:0;top:0;width:744px;height:28px;background:var(--orange)}
.topbar ul{position:absolute;right:14px;top:8px;list-style:none;display:flex;font:400 10px "Arimo",sans-serif;color:var(--white)}
.topbar li+li::before{content:"|";margin:0 9px}

.hero{left:0;top:28px;width:744px;height:253px;background:linear-gradient(110deg,#c89a6c 0%,#8a5a32 35%,#5a3218 60%,#b07844 85%,#d8b088 100%)}
.brand{left:36px;top:62px;display:flex;align-items:center;gap:7px;color:var(--white);font:700 17px "Asap",sans-serif}
.brand .dot{width:11px;height:11px;border-radius:50%;background:var(--orange)}
.brand-url{left:54px;top:86px;color:var(--white);font:700 17px "Asap",sans-serif;font-size:9px}

.nav{left:245px;top:73px;height:42px;display:flex;background:var(--white);box-shadow:0 2px 4px rgba(0,0,0,.3)}
.nav a{display:block;padding:0 16px;font:500 14px "Asap",sans-serif;line-height:42px;color:#222;text-decoration:none;border-right:1px solid #ddd}
.nav a:last-child{border-right:0}
.nav a.active{background:var(--green);color:var(--white)}
.dots{left:336px;top:259px;display:flex;gap:3px}
.dots span{width:8px;height:9px;background:#111}
.dots span:first-child{background:var(--white)}

.card{top:301px;width:154px;height:162px}
.card .photo{height:131px}
.card .label{height:31px;background:var(--green);color:var(--white);font:500 14px "Asap",sans-serif;line-height:31px;text-align:center}
.card::after{content:"";position:absolute;left:8px;right:8px;bottom:-6px;height:6px;border-radius:50%;background:rgba(0,0,0,.18)}
.card.feature .photo{height:86px}
.card.feature .panel{height:76px;background:var(--orange);color:var(--white);text-align:center;padding:5px 8px}
.panel h3{font:500 14px "Asap",sans-serif;margin-bottom:3px}
.panel p{font:400 8.5px/1.45 "Arimo",sans-serif}
.panel .more{font:400 8.5px "Arimo",sans-serif;color:#222}

.welcome-photo{left:32px;top:494px;width:243px;height:186px;border:3px solid var(--orange);background:linear-gradient(135deg,#bfc5c4,#e8e6e0 45%,#9aa09c)}
.welcome-title{left:292px;top:490px;font:700 34px "Asap",sans-serif;color:var(--green)}
.welcome-sub{left:339px;top:530px;font:400 24px "Asap",sans-serif;color:var(--orange)}
.welcome-text{left:292px;top:570px;width:226px;font:400 9.3px/1.65 "Arimo",sans-serif;color:#666}
.btn{left:292px;top:659px;width:61px;height:21px;background:var(--green);color:var(--white);font:400 9px "Arimo",sans-serif;line-height:21px;text-align:center}

.blog{left:535px;top:494px;width:176px;height:188px;border:1px solid var(--light)}
.blog h4{margin:4px;height:28px;background:var(--green);color:var(--white);font:500 12px "Asap",sans-serif;line-height:28px;padding-left:6px}
.blog .title{left:85px;top:60px;font:400 16px/1.05 "Asap",sans-serif;color:var(--orange)}
.blog .meta{left:85px;top:96px;font:400 11px/1.6 "Asap",sans-serif;color:#999}
.blog .excerpt{left:11px;top:136px;width:150px;font:400 10px/1.55 "Arimo",sans-serif;color:#bbb}

.section-title{left:32px;top:713px;font:400 25px "Asap",sans-serif;color:var(--orange)}
.rule{left:32px;width:679px;height:1px;background:var(--light)}
.thumb{top:751px;width:154px;height:82px}

.video{left:32px;top:852px;width:679px;height:231px;background:linear-gradient(100deg,#6d6a64 0%,#a9a39a 25%,#5a4a3c 50%,#7a4430 68%,#c4b8a8 85%,#8a8276 100%)}
.video h2{position:absolute;left:0;right:0;top:160px;text-align:center;font:400 19px "Asap",sans-serif;color:var(--white)}
.video p{position:absolute;left:0;right:0;top:190px;text-align:center;font:400 8.5px "Arimo",sans-serif;color:var(--white)}

.footer{left:0;top:1096px;width:744px;height:104px;background:var(--dark);color:#eee}
.footer h5{font:400 11px "Asap",sans-serif;color:var(--white)}
.footer .addr{font:400 9px/1.6 "Arimo",sans-serif}
.newsletter-input{left:279px;top:49px;width:138px;height:26px;background:#2a2a2a}
.newsletter-btn{left:417px;top:49px;width:48px;height:26px;background:var(--orange);color:var(--white);font:400 9px "Arimo",sans-serif;line-height:26px;text-align:center}
.copy{left:549px;top:24px;font:400 9px "Arimo",sans-serif;color:var(--white)}
.social{left:576px;top:52px;display:flex;gap:8px}
.social span{width:20px;height:20px;border-radius:50%;background:var(--white)}
</style>
</head>
<body>

<div class="abs topbar">
  <ul><li>Recipes</li><li>Health &amp; Wellness</li><li>Confidentiality</li><li>Affordability</li><li>Friday Cocktails</li></ul>
</div>

<div class="abs hero" role="img" aria-label="Diner serving a plate of roasted food at a restaurant table"></div>
<div class="abs brand"><span class="dot"></span>Our Pantry Remedy</div>
<div class="abs brand-url">OurPantryRemedy.example</div>
<nav class="abs nav">
  <a class="active">HOME</a><a>ABOUT</a><a>SERVICES</a><a>ARTICLES</a><a>BLOG</a><a>CONTACT</a>
</nav>
<div class="abs dots"><span></span><span></span><span></span><span></span><span></span><span></span></div>

<div class="abs card" style="left:32px">
  <div class="photo" role="img" aria-label="Chef presenting dishes in a kitchen" style="background:linear-gradient(160deg,#8c8a80,#d8d4c8 50%,#6c5a44)"></div>
  <div class="label">RECIPES</div>
</div>
<div class="abs card feature" style="left:206px">
  <div class="photo" role="img" aria-label="Couple dancing in a banquet hall" style="background:linear-gradient(160deg,#5a2a18,#b86a3a 50%,#3a2a20)"></div>
  <div class="panel">
    <h3>CONFIDENTIALITY</h3>
    <p>Contrary to popular belief, Lorem Ipsum is not simply random text. It has roots in a piece of classical</p>
    <div class="more">More...</div>
  </div>
</div>
<div class="abs card" style="left:381px">
  <div class="photo" role="img" aria-label="Staff exchanging a card at a service counter" style="background:linear-gradient(160deg,#6a5a48,#a08a6c 50%,#4a3a2c)"></div>
  <div class="label">AFFORDABILITY</div>
</div>
<div class="abs card" style="left:557px">
  <div class="photo" role="img" aria-label="Singer performing with a band on stage" style="background:linear-gradient(160deg,#1a2a3a,#6a5a5a 50%,#2a1a1a)"></div>
  <div class="label">FRIDAY COCKTAILS</div>
</div>

<div class="abs welcome-photo" role="img" aria-label="Smiling chef holding kitchen knives"></div>
<div class="abs welcome-title">WELCOME</div>
<div class="abs welcome-sub">TO OUR PLACE...</div>
<p class="abs welcome-text">Lorem Ipsum is simply dummy text of the printing and typesetting industry. Lorem Ipsum has been the indus­try's standard dummy text ever since the 1500s, when an unknown printer took a galley of type and scram­bled it to make a type specimen book.</p>
<div class="abs btn">Read More...</div>

<div class="abs blog">
  <h4>RECENT BLOG</h4>
  <svg class="abs" style="left:11px;top:58px" width="53" height="68" viewBox="0 0 53 68" aria-hidden="true">
    <rect x="0" y="6" width="53" height="62" fill="#c8c8c8"/>
    <rect x="8" y="30" width="37" height="30" fill="#fff"/>
    <rect x="10" y="0" width="5" height="14" fill="#9a9a9a"/>
    <rect x="38" y="0" width="5" height="14" fill="#9a9a9a"/>
    <text x="26.5" y="52" text-anchor="middle" font-family="Asap, sans-serif" font-size="17" fill="#333">18</text>
  </svg>
  <div class="abs title">PELENTE<br>MOR.</div>
  <div class="abs meta">IPSUM DOLORE<br>COM</div>
  <p class="abs excerpt">Lorem ipsum dolor sit amt consetes ctetur adipiscin.</p>
</div>

<div class="abs section-title">WHAT'S NEW</div>
<svg class="abs" style="left:675px;top:719px" width="36" height="20" viewBox="0 0 36 20" aria-hidden="true">
  <path d="M13 2 L5 10 L13 18" fill="none" stroke="#f0602a" stroke-width="4"/>
  <path d="M23 2 L31 10 L23 18" fill="none" stroke="#f0602a" stroke-width="4"/>
</svg>
<div class="abs rule" style="top:745px"></div>
<div class="abs thumb" style="left:32px;background:linear-gradient(135deg,#d8b890,#8a5a30)" role="img" aria-label="Baked pastry dish"></div>
<div class="abs thumb" style="left:206px;background:linear-gradient(135deg,#4a3a20,#e8d8a0 55%,#6a5a30)" role="img" aria-label="Pasta plate with wine glasses"></div>
<div class="abs thumb" style="left:381px;background:linear-gradient(135deg,#5a5a5a,#c8c0b8 50%,#7a3a2a)" role="img" aria-label="Chef carrying plated meals"></div>
<div class="abs thumb" style="left:557px;background:linear-gradient(135deg,#e8e4dc,#c87050 55%,#5a6a3a)" role="img" aria-label="Plated seafood with garnish"></div>
<div class="abs rule" style="top:840px"></div>

<div class="abs video" role="img" aria-label="Chefs plating dishes in a busy restaurant kitchen">
  <svg class="abs" style="left:320px;top:97px" width="48" height="48" viewBox="0 0 48 48" aria-hidden="true">
    <circle cx="24" cy="24" r="24" fill="#111"/>
    <path d="M19 14 L35 24 L19 34 Z" fill="#fff"/>
  </svg>
  <h2>PLAN YOUR NEXT GREAT FOOD TRIP</h2>
  <p>EXPERIENCE EXCITING DISHES FROM ALL OVER THE WORLD</p>
</div>

<footer class="abs footer">
  <svg class="abs" style="left:34px;top:23px" width="11" height="15" viewBox="0 0 11 15" aria-hidden="true">
    <path d="M5.5 0 C2.5 0 0 2.4 0 5.4 C0 9.3 5.5 15 5.5 15 C5.5 15 11 9.3 11 5.4 C11 2.4 8.5 0 5.5 0 Z" fill="#f0602a"/>
    <circle cx="5.5" cy="5.4" r="2" fill="#3b3b3b"/>
  </svg>
  <h5 class="abs" style="left:53px;top:22px">CONTACT US</h5>
  <div class="abs addr" style="left:57px;top:41px">212, Lane No-4,<br>Harbor Road, USA - 330120</div>
  <div class="abs addr" style="left:57px;top:71px">000-0000-000</div>
  <h5 class="abs" style="left:280px;top:22px">SIGN UP FOR NEWSLETTER</h5>
  <div class="abs newsletter-input"></div>
  <div class="abs newsletter-btn">SUBMIT</div>
  <div class="abs copy">DANA CORWELL © 2014 | PRIVACY POLICY</div>
  <div class="abs social">
    <span aria-label="Friendloop"></span><span aria-label="chirpel"></span><span aria-label="Pinvora"></span><span aria-label="Linkroster"></span>
  </div>
</footer>

</body>
</html>
```